Best in class business looking for best in class stationery that accurately reflects the brand image we are trying to build as the brand expands throughout the country. The Varying items should be an eye catching design that makes even the simplest letter or small business card stand out in the crowd.

Target Market(s)

Professionals

Industry/Entity Type

Real Estate

Other font styles liked:
• See atttached logo

Requirements
Must have
• Letterhead
• Business cards
• Envelopes
• Labels for larger mailings
Nice to have
• Folders
• Notebook
Should not have
• Stale design elements

```html
<!DOCTYPE html>
<html lang="en">
<head>
<meta charset="utf-8">
<title>Ridgeline Property Group – Business Card</title>
<link href="https://fonts.googleapis.com/css2?family=Open+Sans:wght@400;600&display=swap" rel="stylesheet">
<style>
  :root{
    --navy:#1e2a86;
    --navy-deep:#141c5e;
    --blue:#3448b0;
    --blue-light:#5d72cc;
    --ink:#333a48;
    --grey:#5e6470;
    --rule:#9aa0a8;
    --paper:#ffffff;
    --backdrop:#e9eaec;
  }
  *{margin:0;padding:0;box-sizing:border-box}
  html,body{width:1200px;height:843px;overflow:hidden}
  body{
    background:var(--backdrop);
    font-family:"Open Sans",Arial,sans-serif;
    display:flex;align-items:center;justify-content:center;gap:40px;
  }
  .card{
    position:relative;width:540px;height:309px;overflow:hidden;
    box-shadow:0 6px 18px rgba(0,0,0,.18);
  }
  /* back side */
  .card-back{
    background:linear-gradient(135deg,var(--blue) 0%,var(--navy) 55%,var(--navy-deep) 100%);
    color:var(--paper);
    display:flex;flex-direction:column;align-items:center;justify-content:center;
  }
  .brand{display:flex;align-items:center;gap:12px}
  .brand-mark{width:18px;height:18px;background:currentColor}
  .brand-name{font-weight:600;font-size:25px;letter-spacing:.06em;text-transform:uppercase}
  .card-back .web{margin-top:26px;font-size:12px;letter-spacing:.42em}

  /* front side */
  .card-front{background:var(--paper)}
  .person{position:absolute;left:34px;top:52px}
  .person-name{font-size:18px;font-weight:600;color:var(--navy)}
  .person-title{font-size:13px;color:var(--blue);margin-top:1px}
  .front-rule{position:absolute;left:34px;top:108px;width:472px;height:1px;background:var(--rule)}
  .front-rule.short{left:300px;top:220px;width:206px}
  .contacts{position:absolute;left:34px;top:120px;list-style:none}
  .contacts li{display:flex;align-items:center;gap:12px;font-size:13px;color:var(--ink);height:20px}
  .contacts svg{width:14px;height:14px;fill:var(--navy)}
  .card-front .brand{position:absolute;right:34px;top:66px;color:var(--navy)}
  .card-front .brand-name{font-size:19px}
  .card-front .brand-mark{width:14px;height:14px}
  .address{position:absolute;right:34px;top:230px;text-align:right;font-size:13px;color:var(--grey);line-height:19px}
  .address .web{letter-spacing:.22em}
  .base-band{position:absolute;left:0;bottom:0;width:100%;height:16px}
</style>
</head>
<body>
  <section class="card card-back" aria-label="Card back">
    <div class="brand"><span class="brand-mark"></span><span class="brand-name">Ridgeline Property Group</span></div>
    <div class="web">www.ridgelinepg.com</div>
  </section>

  <section class="card card-front" aria-label="Card front">
    <div class="person">
      <div class="person-name">Mark Ellison</div>
      <div class="person-title">President</div>
    </div>
    <div class="front-rule"></div>
    <ul class="contacts">
      <li><svg viewBox="0 0 16 16"><path d="M3 2h3l1.5 3.5-2 1.3a8 8 0 0 0 3.7 3.7l1.3-2L14 10v3a1 1 0 0 1-1 1A11 11 0 0 1 2 3a1 1 0 0 1 1-1z"/></svg>555 0142 7781</li>
      <li><svg viewBox="0 0 16 16"><path d="M5 1h6a1 1 0 0 1 1 1v12a1 1 0 0 1-1 1H5a1 1 0 0 1-1-1V2a1 1 0 0 1 1-1zm0 2v9h6V3zm3 10a.8.8 0 1 0 0 .01z"/></svg>555 0198 3364</li>
      <li><svg viewBox="0 0 16 16"><path d="M4 1h6l2 2v3h1a2 2 0 0 1 2 2v6H1V8a2 2 0 0 1 2-2h1zm1 1v4h6V3.5L9.5 2zm-1 8v2h8v-2z"/></svg>555 0173 2209</li>
      <li><svg viewBox="0 0 16 16"><path d="M1 3h14v10H1zm1.5 1.2L8 8.5l5.5-4.3z"/></svg>mark@ridgelinepg.com</li>
    </ul>
    <div class="brand"><span class="brand-mark"></span><span class="brand-name">Ridgeline Property Group</span></div>
    <div class="front-rule short"></div>
    <div class="address">
      <div>1720 Harbor View Lane</div>
      <div>Cedar Falls, NY 10990</div>
      <div class="web">www.ridgelinepg.com</div>
    </div>
    <svg class="base-band" viewBox="0 0 540 16" preserveAspectRatio="none" aria-hidden="true">
      <rect width="540" height="16" fill="var(--navy)"/>
      <polygon points="130,0 248,0 240,16 122,16" fill="var(--blue-light)"/>
      <polygon points="255,0 540,0 540,16 247,16" fill="var(--blue)"/>
    </svg>
  </section>
</body>
</html>
```